Fishing Tackle Product Packaging Backdrop/Template

Hi Designers,
we require a versatile packaging backdrop/template design for our fishing tackle brand. The design will be used in printed packaging for a range of products from small to large so would need to be scaleable. It will most commonly be used on small printed card tags (2x3"), but we would like to be able to use it for other packaging aswell.
A section for our product details, which we can edit ourselves would be essential, this way we can use the template for any of our products. The back of the card will need a space for our barcodes.
The design needs to be predominantly macsuline and appeal to the modern carp angler. It also needs to pop so that our goods really stand out against our competitors. Please see our logo attached. It'd also be great to see our web address at the bottom, on both sides of the design: www.brelvanrigs.co.uk

Thanks in advance and good luck!
Brelvan Rigs Team
Updates

Target Market(s)

Male Carp Anglers (aprox ages 18-60)

Industry/Entity Type

Fishing Tackle

Requirements
Must have
• Our logo and web address, with a section for a barcode and product title/info

```html
<!DOCTYPE html>
<html lang="en">
<head>
<meta charset="utf-8">
<title>Brelvan Rigs – Tackle Card Tag</title>
<link href="https://fonts.googleapis.com/css2?family=Poppins:wght@400;500;600&display=swap" rel="stylesheet">
<style>
  :root {
    --backdrop: #e0dedf;
    --card-green: #435436;
    --forest-dark: #1f2a1e;
    --grass: #5f7d35;
    --sky-top: #d9614a;
    --sky-low: #e5914a;
    --sun: #f0c15a;
    --water: #1e6a85;
    --water-light: #5ea5bb;
    --panel: #fafafa;
    --muted-text: #7a7a7a;
    --ink: #222222;
    --white: #ffffff;
  }
  * { box-sizing: border-box; margin: 0; padding: 0; }
  html, body {
    width: 1017px; height: 1200px; overflow: hidden;
    background: var(--backdrop);
    font-family: "Poppins", sans-serif;
  }
  .tag-set { position: relative; width: 1017px; height: 1200px; }
  .tag { position: absolute; top: 261px; width: 348px; height: 677px; }
  .tag--front { left: 134px; }
  .tag--back { left: 534px; }
  .tag svg { display: block; width: 348px; height: 677px; }
  .brand-mark {
    position: absolute; left: 126px; top: 75px; width: 96px; height: 96px;
    border-radius: 50%; background: var(--white);
    display: flex; align-items: center; justify-content: center; text-align: center;
    color: var(--card-green); font-weight: 600; font-size: 14px; line-height: 1.15;
  }
  .details-panel {
    position: absolute; left: 50px; top: 193px; width: 247px; height: 439px;
    border-radius: 18px; background: var(--panel);
    display: flex; align-items: center; justify-content: center; text-align: center;
    color: var(--muted-text); font-size: 16px; line-height: 1.2;
  }
  .barcode-box {
    position: absolute; left: 59px; top: 580px; width: 240px; height: 64px;
    border-radius: 8px; background: var(--white);
    display: flex; align-items: center; justify-content: center;
    color: var(--ink); font-size: 16px; font-weight: 500;
  }
  .web-address {
    position: absolute; left: 0; right: 0; text-align: center;
    color: var(--white); font-size: 15px; font-weight: 600; letter-spacing: 0.2px;
    line-height: 22px;
  }
  .tag--back .web-address { top: 652px; }
  .tag--front .web-address { top: 643px; }
</style>
</head>
<body>
<main class="tag-set">

  <section class="tag tag--front">
    <svg viewBox="0 0 348 677" xmlns="http://www.w3.org/2000/svg">
      <defs>
        <mask id="front-shape">
          <path fill="#fff" d="M20 0H328Q348 0 348 20V122L326 148L348 174V657Q348 677 328 677H20Q0 677 0 657V174L22 148L0 122V20Q0 0 20 0Z"/>
          <rect x="107" y="42" width="134" height="24" rx="12" fill="#000"/>
          <circle cx="174" cy="44" r="16" fill="#000"/>
        </mask>
        <linearGradient id="forest-fill" x1="0" y1="0" x2="0" y2="1">
          <stop offset="0" stop-color="var(--forest-dark)"/>
          <stop offset="0.35" stop-color="var(--grass)"/>
          <stop offset="0.75" stop-color="#3f5a2a"/>
          <stop offset="1" stop-color="var(--forest-dark)"/>
        </linearGradient>
      </defs>
      <g mask="url(#front-shape)">
        <rect class="card-base" width="348" height="677" fill="var(--card-green)"/>
        <rect class="forest-scene" role="img" aria-label="Forest treeline and tall grass illustration" y="150" width="348" height="527" fill="url(#forest-fill)"/>
      </g>
    </svg>
    <div class="brand-mark">Brelvan<br>Rigs</div>
    <div class="details-panel">Details<br>about the<br>product<br>Here</div>
    <div class="web-address">BRELVANRIGS.UK</div>
  </section>

  <section class="tag tag--back">
    <svg viewBox="0 0 348 677" xmlns="http://www.w3.org/2000/svg">
      <defs>
        <mask id="back-shape">
          <path fill="#fff" d="M20 0H328Q348 0 348 20V122L326 148L348 174V657Q348 677 328 677H20Q0 677 0 657V174L22 148L0 122V20Q0 0 20 0Z"/>
          <rect x="107" y="42" width="134" height="24" rx="12" fill="#000"/>
          <circle cx="174" cy="44" r="16" fill="#000"/>
        </mask>
        <linearGradient id="lake-fill" x1="0" y1="0" x2="0" y2="1">
          <stop offset="0" stop-color="var(--sky-top)"/>
          <stop offset="0.3" stop-color="var(--sky-low)"/>
          <stop offset="0.45" stop-color="var(--sun)"/>
          <stop offset="0.465" stop-color="#e6e6e6"/>
          <stop offset="0.48" stop-color="var(--water)"/>
          <stop offset="0.65" stop-color="var(--water-light)"/>
          <stop offset="0.88" stop-color="var(--water)"/>
          <stop offset="1" stop-color="var(--grass)"/>
        </linearGradient>
      </defs>
      <g mask="url(#back-shape)">
        <rect class="card-base" width="348" height="677" fill="var(--forest-dark)"/>
        <rect class="lake-scene" role="img" aria-label="Sunset lake scene with a leaping fish caught on a rod and line, reeds in the foreground" width="348" height="570" fill="url(#lake-fill)"/>
      </g>
    </svg>
    <div class="brand-mark">Brelvan<br>Rigs</div>
    <div class="barcode-box">Barcode Here</div>
    <div class="web-address">BRELVANRIGS.UK</div>
  </section>

</main>
</body>
</html>
```